Fully Coded Website - Mind Lantern (Ebook)

Fully coded website selling my Ebook.
The book is on the topic of the law of attraction. The most similar example of something like it is "The Hidden Key (http://www.quillmarrow.example/).
The layout of the website should be a simple one page long selling pitch that builds up to the selling of the ebook with a buy now function (similar to information products found on vendbarrow).
Upon entering the website, the user should immediately receive a pop-up to enter their first name and email address if they want to receive a free email about "10 vital facts about the Law of Attraction".
My book cover (attached) needs to be heavily used throughout the website. Also include the contents page of the book (also attached) wherever/however most appropriate.
Also see the doc attached of famous quotes. These quotes need to be PRESENTED IN A SLIDER FORMAT ONE AT A TIME for a duration of 5 seconds each.
Also see the doc of my introductory statement that needs to be included.
No other books should be included except mine (this is not a storefront for selling any other books except mine).
I am not tech savvy at all so please make the website using a simple format so that I can easily adjust things in the future myself.

```html
<!DOCTYPE html>
<html lang="en">
<head>
<meta charset="utf-8">
<title>The Law Of Attraction – Mind Lantern</title>
<link rel="stylesheet" href="https://fonts.googleapis.com/css2?family=Merriweather:wght@300;400;700&display=swap">
<style>
  :root{
    --brand-blue:#2a7cc7;
    --strip-blue:#1f5fa3;
    --navy:#0d1a45;
    --navy-btn:#0c1b4a;
    --ink:#333333;
    --muted:#8c8c8c;
    --body-text:#4a4a4a;
    --rule:#d6d6d6;
    --panel:#f2f2f2;
    --card:#f8f8f8;
    --white:#ffffff;
  }
  *{box-sizing:border-box;margin:0;padding:0}
  html,body{width:1200px;height:3000px;overflow:hidden}
  body{position:relative;background:var(--white);font-family:"Merriweather",Georgia,serif;color:var(--ink)}
  .abs{position:absolute}

  /* Header */
  .top-strip{left:0;top:0;width:1200px;height:6px;background:var(--strip-blue)}
  .site-header{left:0;top:6px;width:1200px;height:106px;background:var(--white)}
  .nav-link{top:60px;font-size:15px;color:#222;text-decoration:none}
  .brand{display:flex;align-items:center;gap:10px;color:var(--navy);font-size:20px;font-weight:400;white-space:nowrap}
  .brand-mark{width:18px;height:18px;background:var(--brand-blue)}
  .header-brand{left:526px;top:54px;width:150px;justify-content:center}

  /* Hero */
  .hero{left:0;top:112px;width:1200px;height:540px;
    background:radial-gradient(ellipse at 45% 60%, #3f8ee6 0%, #1a4fb0 30%, #0b2466 60%, #040b25 100%)}
  .hero-title{left:0;top:372px;width:1200px;text-align:center;font-size:40px;font-weight:400;color:var(--white);letter-spacing:1px}
  .hero-arrow{top:396px}
  .btn{display:flex;align-items:center;justify-content:center;color:var(--white);text-transform:uppercase;background:var(--navy-btn);font-size:14px;text-decoration:none}
  .hero-btn{left:554px;top:460px;width:150px;height:56px;background:#0a1633;font-size:13px}

  /* Introduction */
  .intro-band{left:0;top:652px;width:1200px;height:696px;background:var(--panel)}
  .intro-card{left:190px;top:748px;width:818px;height:518px;background:var(--white);border:1px solid #e3e3e3}
  .intro-title{left:190px;top:784px;width:818px;text-align:center;font-size:34px;font-weight:700;color:var(--navy)}
  .intro-sub{left:190px;top:830px;width:818px;text-align:center;font-size:24px;font-weight:300;color:#444;letter-spacing:1px}
  .intro-rule{left:404px;top:886px;width:390px;height:1px;background:var(--rule)}
  .intro-text{left:222px;width:754px;text-align:center;font-size:11px;line-height:24px;color:var(--body-text)}
  .intro-btn{left:528px;top:1164px;width:144px;height:40px;font-size:13px}

  /* Quote slider */
  .quotes-title{left:0;top:1400px;width:1200px;text-align:center;font-size:34px;font-weight:700;color:var(--navy)}
  .quote-slide{left:300px;top:1500px;width:600px;height:400px;background:var(--card);box-shadow:0 2px 3px rgba(0,0,0,.12)}
  .quote-text{position:absolute;left:60px;top:110px;width:480px;text-align:center;font-size:20px;line-height:36px;font-weight:300;color:var(--muted)}
  .quote-rule{position:absolute;left:200px;top:286px;width:200px;height:1px;background:var(--rule)}
  .quote-name{position:absolute;left:0;top:314px;width:600px;text-align:center;font-size:22px;font-weight:700;color:var(--navy)}

  /* Book */
  .book-band{left:0;top:2076px;width:1200px;height:622px;background-color:var(--panel);
    background-image:linear-gradient(rgba(0,0,0,.025) 1px,transparent 1px),linear-gradient(90deg,rgba(0,0,0,.025) 1px,transparent 1px);
    background-size:12px 12px}
  .book-cover{left:240px;top:2146px;width:310px;height:496px;
    background:linear-gradient(180deg,#1b2a4a 0%,#2c4a78 35%,#1a2b4f 65%,#3a3050 85%,#0c0c18 100%)}
  .cover-rule{position:absolute;left:14px;width:282px;height:1px;background:rgba(255,255,255,.8)}
  .cover-title{position:absolute;left:0;top:62px;width:310px;text-align:center;color:#fff;font-size:22px;font-weight:300;letter-spacing:1px}
  .cover-sub{position:absolute;left:0;top:90px;width:310px;text-align:center;color:#fff;font-size:13px;font-weight:300}
  .book-heading{left:600px;top:2222px;font-size:62px;line-height:52px;font-weight:700;color:var(--ink)}
  .book-sub{left:600px;top:2396px;font-size:28px;line-height:38px;font-weight:300;color:#555}
  .buy-btn{left:600px;top:2498px;width:174px;height:48px;font-size:16px}

  /* Footer */
  .footer-brand{left:200px;top:2800px;font-size:18px}
  .foot-col h4{font-size:12px;font-weight:700;color:var(--navy);margin-bottom:16px}
  .foot-col p{font-size:12px;line-height:23px;color:#333}
  .foot-rule{left:200px;top:2944px;width:800px;height:1px;background:#e2e2e2}
  .foot-small{top:2964px;font-size:11px;color:#666}
  .social{top:2958px;width:24px;height:24px;border-radius:50%;background:var(--strip-blue)}
</style>
</head>
<body>

<header>
  <div class="abs top-strip"></div>
  <div class="abs site-header"></div>
  <nav>
    <a class="abs nav-link" style="left:288px" href="#">Home</a>
    <a class="abs nav-link" style="left:362px" href="#">Stories</a>
    <a class="abs nav-link" style="left:442px" href="#">About</a>
    <div class="abs brand header-brand"><span class="brand-mark"></span>Mind Lantern</div>
    <a class="abs nav-link" style="left:702px" href="#">Products</a>
    <a class="abs nav-link" style="left:792px" href="#">Faq's</a>
    <a class="abs nav-link" style="left:864px" href="#">Contact Us</a>
  </nav>
</header>

<section>
  <div class="abs hero" role="img" aria-label="Glowing blue energy waves with light particles"></div>
  <svg class="abs hero-arrow" style="left:146px" width="20" height="30" viewBox="0 0 20 30"><path d="M16 3 L5 15 L16 27" fill="none" stroke="#fff" stroke-width="4"/></svg>
  <svg class="abs hero-arrow" style="left:1034px" width="20" height="30" viewBox="0 0 20 30"><path d="M4 3 L15 15 L4 27" fill="none" stroke="#fff" stroke-width="4"/></svg>
  <h1 class="abs hero-title">The&nbsp; Law Of&nbsp; Attraction</h1>
  <a class="abs btn hero-btn" href="#">Learn More</a>
</section>

<section>
  <div class="abs intro-band"></div>
  <div class="abs intro-card"></div>
  <h2 class="abs intro-title">INTRODUCTION</h2>
  <p class="abs intro-sub">The&nbsp; Law Of&nbsp; Attraction</p>
  <div class="abs intro-rule"></div>
  <p class="abs intro-text" style="top:928px">The law of attraction has for long fascinated and marvelled me. I first experienced its energies subconsciously in adolescence. Since then I have used it to get into medical school and become a doctor, grow taller in my twenties, become a successful entrepreneur and marry my soul mate. Over time, through the study of numerous books and the lives of the most successful people in history, I came to the realisation that success is no coincidence. Although there isn't a simple formula for success, there is one fundamentally vital ingredient!</p>
  <p class="abs intro-text" style="top:1048px">I will walk you through the law of attraction through the eyes of history and into the modern era. We will see how key figures in the philosophy and study of the force have described it and how the most successful of figures have harnessed its powers. Finally, I will teach you how to practically implement the law of attraction in your daily life in order to achieve the life of your dreams!</p>
  <a class="abs btn intro-btn" href="#">Contact Us</a>
</section>

<section>
  <h2 class="abs quotes-title">Our Quotes</h2>
  <div class="abs quote-slide">
    <p class="quote-text">Be thankful for what you have; you'll end up having more. If you concentrate on what you don't have, you will never ever have enough.</p>
    <div class="quote-rule"></div>
    <p class="quote-name">Ora Wendell</p>
  </div>
  <svg class="abs" style="left:572px;top:1988px" width="14" height="20" viewBox="0 0 14 20"><path d="M11 2 L3 10 L11 18" fill="none" stroke="#c4c4c4" stroke-width="2.5"/></svg>
  <svg class="abs" style="left:614px;top:1988px" width="14" height="20" viewBox="0 0 14 20"><path d="M3 2 L11 10 L3 18" fill="none" stroke="#c4c4c4" stroke-width="2.5"/></svg>
</section>

<section>
  <div class="abs book-band"></div>
  <div class="abs book-cover" role="img" aria-label="Book cover: starry night sky with a shooting star over a dark hill">
    <div class="cover-rule" style="top:52px"></div>
    <p class="cover-title">THE MIND LANTERN</p>
    <p class="cover-sub">Unveiling the Law of Attraction</p>
    <div class="cover-rule" style="top:112px"></div>
  </div>
  <h2 class="abs book-heading">The<br>Mind<br>Lantern</h2>
  <p class="abs book-sub">Unveiling the law of<br>Attraction</p>
  <a class="abs btn buy-btn" href="#">Buy Now</a>
</section>

<footer>
  <div class="abs brand footer-brand"><span class="brand-mark"></span>Mind Lantern</div>
  <div class="abs foot-col" style="left:394px;top:2738px">
    <h4>Quick Links</h4>
    <p>Home<br>Stories<br>About<br>Products<br>Faq's<br>Contact Us</p>
  </div>
  <div class="abs foot-col" style="left:590px;top:2738px">
    <h4>Other Links</h4>
    <p>Terms Of USe<br>Privacy Policy<br>Career</p>
  </div>
  <div class="abs foot-col" style="left:794px;top:2738px">
    <h4>Contact Us</h4>
    <p>Studio Lanternhaus<br>Lindenweg 12<br>10115 Brookdale<br><br>E-Mail: info@mindlantern.example</p>
  </div>
  <div class="abs foot-rule"></div>
  <p class="abs foot-small" style="left:200px">© 2016 Company Name &nbsp;|&nbsp; All Rihgts Reserved</p>
  <p class="abs foot-small" style="left:740px">Connect With Us</p>
  <div class="abs social" style="left:848px"></div>
  <div class="abs social" style="left:880px"></div>
  <div class="abs social" style="left:912px"></div>
  <div class="abs social" style="left:944px"></div>
  <div class="abs social" style="left:976px"></div>
</footer>

</body>
</html>
```